International Hand & Body company needing a Hand cream tube design for the Retail market

I am wanting a modern design for a new range of 6 hand creams I will be launching in August. They need to compliment our range of wrapped soaps which you can see on www.plomvane.com.au so am wanting clean designs. I am wanting a solid colour with a hand drawn organic feel line drawing in black elegantly placed wrapping around the label. I am wanting to focus on the colour and positioning of words and fonts. I like modern clean contemporary fonts. The final design needs to appeal to the broader female market.This may lead to range expansion if designs are well received.
Updates

These designs are not hitting the brief. They are too generic and look like a supermarket brand. Our brand is more boutique and this design needs to be modern and simple. I would like more solid colours and more modern designs. Without patterns.

Target Market(s)

Female aged 20 - 70

Requirements
Must have
• a modern contemporary design that will appeal to the masses.
• Please read attached brief.
Should not have
• a black botanical illustration, in a loose and organic design to match the fragrance.

```html
<!DOCTYPE html>
<html lang="en">
<head>
<meta charset="utf-8">
<title>plomvane hand cream range</title>
<link href="https://fonts.googleapis.com/css2?family=Amatic+SC:wght@400&family=Josefin+Sans:wght@400&family=Special+Elite&display=swap" rel="stylesheet">
<style>
  :root {
    --canvas: #ffffff;
    --ink: #111111;
    --cap: #4a4a4a;
    --cap-shade: #3a3a3a;
    --green-light: #c2e2c0;
    --green-band: #6bae70;
    --green-copy: #5ea363;
    --pink-light: #f3c0c9;
    --pink-band: #e8808f;
    --pink-copy: #e27887;
    --blue-light: #a2c0ea;
    --blue-band: #4f7fd3;
    --blue-copy: #4a78cc;
  }
  html, body {
    margin: 0;
    padding: 0;
    overflow: hidden;
    background: var(--canvas);
  }
  .range {
    position: relative;
    width: 1200px;
    height: 829px;
    overflow: hidden;
    background: var(--canvas);
  }
  .tube {
    position: absolute;
    top: 158px;
    width: 254px;
    height: 550px;
  }
  .tube--bergamot { left: 126px; --light: var(--green-light); --band: var(--green-band); --copy: var(--green-copy); }
  .tube--rose { left: 477px; --light: var(--pink-light); --band: var(--pink-band); --copy: var(--pink-copy); }
  .tube--jasmine { left: 824px; --light: var(--blue-light); --band: var(--blue-band); --copy: var(--blue-copy); }

  .tube__shape { position: absolute; inset: 0; }
  .tube__body { fill: var(--light); }
  .tube__band { fill: var(--band); }
  .tube__streak { fill: #ffffff; opacity: 0.45; }
  .tube__cap { fill: var(--cap); }
  .tube__cap-rim { fill: var(--cap-shade); }

  .brand {
    position: absolute;
    top: 40px;
    left: 0;
    width: 254px;
    text-align: center;
    font-family: "Josefin Sans", sans-serif;
    font-weight: 400;
    font-size: 42px;
    letter-spacing: 5px;
    color: var(--ink);
    margin: 0;
  }
  .scent-main {
    position: absolute;
    top: 164px;
    left: 32px;
    font-family: "Special Elite", monospace;
    font-size: 25px;
    color: #2a2a2a;
    margin: 0;
    white-space: nowrap;
  }
  .tube--jasmine .scent-main { font-size: 21px; top: 170px; }
  .scent-note {
    position: absolute;
    top: 212px;
    left: 78px;
    font-family: "Amatic SC", cursive;
    font-size: 62px;
    line-height: 1;
    color: rgba(255,255,255,0.72);
    margin: 0;
    white-space: nowrap;
  }
  .product-type {
    position: absolute;
    top: 298px;
    left: 0;
    width: 254px;
    text-align: center;
    font-family: "Josefin Sans", sans-serif;
    font-size: 17px;
    color: #ffffff;
    margin: 0;
  }
  .claim {
    position: absolute;
    top: 392px;
    right: 57px;
    width: 120px;
    text-align: right;
    font-family: "Josefin Sans", sans-serif;
    font-size: 11px;
    line-height: 13.5px;
    color: var(--copy);
    margin: 0;
  }
</style>
</head>
<body>
<main class="range">

  <article class="tube tube--bergamot">
    <svg class="tube__shape" viewBox="0 0 254 550" width="254" height="550" aria-hidden="true">
      <path class="tube__body" d="M0 0 H254 L214 462 H40 Z"/>
      <path class="tube__band" d="M16 202 L236 186 L221 372 L40 382 Z"/>
      <path class="tube__streak" d="M42 384 L220 370 L219 380 L43 392 Z"/>
      <rect class="tube__cap" x="48" y="462" width="158" height="86" rx="4"/>
      <rect class="tube__cap-rim" x="48" y="540" width="158" height="8" rx="3"/>
    </svg>
    <h2 class="brand">plomvane</h2>
    <p class="scent-main">BERGAMOT</p>
    <p class="scent-note">&amp; AMBER</p>
    <p class="product-type">hand cream</p>
    <p class="claim">a nourishing non-greasy hand cream to keep skin soft &amp; hydrated</p>
  </article>

  <article class="tube tube--rose">
    <svg class="tube__shape" viewBox="0 0 254 550" width="254" height="550" aria-hidden="true">
      <path class="tube__body" d="M0 0 H254 L214 462 H40 Z"/>
      <path class="tube__band" d="M16 202 L236 186 L221 372 L40 382 Z"/>
      <path class="tube__streak" d="M42 384 L220 370 L219 380 L43 392 Z"/>
      <rect class="tube__cap" x="48" y="462" width="158" height="86" rx="4"/>
      <rect class="tube__cap-rim" x="48" y="540" width="158" height="8" rx="3"/>
    </svg>
    <h2 class="brand">plomvane</h2>
    <p class="scent-main">WILD ROSE</p>
    <p class="scent-note">&amp; NEROLI</p>
    <p class="product-type">hand cream</p>
    <p class="claim">a nourishing non-greasy hand cream to keep skin soft &amp; hydrated</p>
  </article>

  <article class="tube tube--jasmine">
    <svg class="tube__shape" viewBox="0 0 254 550" width="254" height="550" aria-hidden="true">
      <path class="tube__body" d="M0 0 H254 L214 462 H40 Z"/>
      <path class="tube__band" d="M16 206 L236 190 L221 376 L40 386 Z"/>
      <path class="tube__streak" d="M42 388 L220 374 L219 384 L43 396 Z"/>
      <rect class="tube__cap" x="48" y="462" width="158" height="86" rx="4"/>
      <rect class="tube__cap-rim" x="48" y="540" width="158" height="8" rx="3"/>
    </svg>
    <h2 class="brand">plomvane</h2>
    <p class="scent-main">WHITE JAMSINE</p>
    <p class="scent-note">&amp; VIOLET</p>
    <p class="product-type">hand cream</p>
    <p class="claim">a nourishing non-greasy hand cream to keep skin soft &amp; hydrated</p>
  </article>

</main>
</body>
</html>
```